New locally owned rental company needs a flyer to circulate

Need flyer with logo, phone# and address. We rent cars to anyone with driver's license and proper insurance. Rates as low as $50/day. Can offer compact cars, mid-size and full size sedans. Also SUV's.

```html
<!DOCTYPE html>
<html lang="en">
<head>
<meta charset="utf-8">
<title>RoadReady Car &amp; Van Rental Flyer</title>
<link href="https://fonts.googleapis.com/css2?family=Poppins:ital,wght@0,400;0,500;0,700;0,800;1,700;1,800;1,900&display=swap" rel="stylesheet">
<style>
  :root {
    --page-bg: #bdbdbd;
    --ink-dark: #262626;
    --brand-blue: #0d4fa8;
    --brand-green: #2fad4e;
    --paper: #f6f7fb;
    --white: #ffffff;
    --text-dark: #1d1d1d;
  }
  * { margin: 0; padding: 0; box-sizing: border-box; }
  html, body { width: 1200px; height: 1080px; overflow: hidden; }
  body { background: var(--page-bg); font-family: "Poppins", sans-serif; position: relative; }

  .flyer {
    position: absolute; left: 213px; top: 40px;
    width: 774px; height: 1000px; overflow: hidden;
    background: var(--ink-dark);
  }
  .flyer > * { position: absolute; }

  .hero-photo {
    left: 0; top: 0; width: 774px; height: 400px;
    background:
      linear-gradient(to bottom, rgba(38,38,38,0) 70%, var(--ink-dark) 100%),
      linear-gradient(to bottom, #b9d2ea 0%, #dfe6ee 30%, #c9cdd2 55%, #6c6e72 80%, #4a4b4e 100%);
  }
  .backdrop-shapes { left: 0; top: 0; width: 774px; height: 1000px; }

  .brand { left: 60px; top: 72px; width: 300px; text-align: center; }
  .brand-name { font-weight: 800; font-size: 44px; line-height: 1; color: var(--brand-blue); letter-spacing: -1px; }
  .brand-sub { margin-top: 8px; font-weight: 700; font-style: italic; font-size: 17px; letter-spacing: 5px; color: var(--text-dark); }

  .headline {
    left: 58px; top: 354px; white-space: nowrap;
    font-weight: 900; font-style: italic; font-size: 90px; line-height: 1; letter-spacing: -3px;
    -webkit-text-stroke: 3px var(--white); paint-order: stroke fill;
    text-shadow: 0 4px 6px rgba(0,0,0,0.35);
  }
  .headline .blue { color: var(--brand-blue); }
  .headline .green { color: var(--brand-green); }

  .requirements { left: 60px; top: 472px; color: var(--white); }
  .requirements-intro { font-size: 22px; font-weight: 400; margin-left: 6px; }
  .requirement { display: flex; align-items: center; gap: 10px; margin-top: 10px; font-weight: 800; font-style: italic; font-size: 31px; line-height: 1.15; }
  .requirement svg { width: 30px; height: 32px; }

  .price { left: 468px; top: 462px; width: 260px; height: 165px; }
  .price-amount {
    position: absolute; left: 34px; top: 6px;
    font-weight: 900; font-style: italic; font-size: 98px; line-height: 1; color: var(--brand-blue); letter-spacing: -2px;
    -webkit-text-stroke: 2px var(--white); paint-order: stroke fill;
  }
  .price-note { position: absolute; left: 29px; top: 116px; font-size: 14px; color: var(--text-dark); }
  .price-unit { position: absolute; left: 156px; top: 110px; font-size: 21px; font-weight: 800; font-style: italic; color: var(--brand-blue); }

  .fleet-gallery { left: 52px; top: 618px; width: 378px; height: 218px; display: grid; grid-template-columns: 1fr 1fr; gap: 4px; }
  .fleet-photo { border: 2px solid var(--white); }
  .fleet-photo.suv-gray { background: linear-gradient(160deg, #a9b9c7 0%, #6b6e72 45%, #5e7a45 100%); }
  .fleet-photo.sedan-blue { background: linear-gradient(160deg, #b7c5d1 0%, #2f3fa0 55%, #6d6f73 100%); }
  .fleet-photo.sedan-red { background: linear-gradient(160deg, #d7dbe0 0%, #b1252d 55%, #77797c 100%); }
  .fleet-photo.suv-silver { background: linear-gradient(160deg, #c0a98c 0%, #b4b6b9 50%, #6f7174 100%); }

  .offer { left: 476px; top: 644px; }
  .offer-title { font-weight: 800; font-style: italic; font-size: 29px; color: var(--brand-blue); letter-spacing: -0.5px; text-shadow: 0 2px 3px rgba(0,0,0,0.25); }
  .offer-list { list-style: none; margin-top: 6px; }
  .offer-list li { font-size: 22px; line-height: 30px; color: var(--text-dark); padding-left: 22px; position: relative; }
  .offer-list li::before { content: ""; position: absolute; left: 0; top: 15px; width: 6px; height: 6px; background: var(--brand-blue); }

  .ribbons { left: 0; top: 790px; width: 774px; height: 120px; }
  .ribbon-text { font-family: "Poppins", sans-serif; font-weight: 800; font-style: italic; font-size: 18px; fill: var(--white); }

  .contact { left: 56px; top: 900px; width: 700px; display: flex; align-items: center; color: var(--white); }
  .contact-phone { display: flex; align-items: center; gap: 12px; font-weight: 800; font-style: italic; font-size: 46px; letter-spacing: -1px; }
  .contact-phone svg, .contact-address svg { flex: none; }
  .contact-address { display: flex; align-items: center; gap: 10px; margin-left: 24px; font-size: 15px; line-height: 1.3; }
</style>
</head>
<body>
<div class="flyer">
  <div class="hero-photo" role="img" aria-label="Photo of three compact sedans parked in front of the rental office building"></div>

  <svg class="backdrop-shapes" viewBox="0 0 774 1000" aria-hidden="true">
    <defs>
      <linearGradient id="panelFade" x1="0" y1="0" x2="0" y2="1">
        <stop offset="0" stop-color="#f6f7fb" stop-opacity="0"/>
        <stop offset="0.08" stop-color="#f6f7fb"/>
        <stop offset="1" stop-color="#f6f7fb"/>
      </linearGradient>
    </defs>
    <polygon points="470,350 774,350 774,830 380,830 456,366" fill="url(#panelFade)"/>
    <polygon points="0,58 420,32 420,212 0,238" fill="#ffffff"/>
    <ellipse cx="596" cy="542" rx="128" ry="78" fill="none" stroke="#0d4fa8" stroke-width="3" transform="rotate(-8 596 542)"/>
  </svg>

  <div class="brand">
    <div class="brand-name">RoadReady</div>
    <div class="brand-sub">Car &amp; Van Rental</div>
  </div>

  <div class="headline"><span class="blue">NEED</span> <span class="green">A CAR?</span></div>

  <div class="requirements">
    <p class="requirements-intro">We rent cars to anyone with</p>
    <p class="requirement">
      <svg viewBox="0 0 30 32"><rect x="1" y="8" width="20" height="20" fill="#ffffff"/><path d="M5 17 L11 24 L27 2" fill="none" stroke="#0d4fa8" stroke-width="4.5" stroke-linecap="round"/></svg>
      DRIVER'S LICENSE
    </p>
    <p class="requirement">
      <svg viewBox="0 0 30 32"><rect x="1" y="8" width="20" height="20" fill="#ffffff"/><path d="M5 17 L11 24 L27 2" fill="none" stroke="#0d4fa8" stroke-width="4.5" stroke-linecap="round"/></svg>
      INSURANCE
    </p>
  </div>

  <div class="price">
    <div class="price-amount">$50</div>
    <div class="price-note">Rates as low as</div>
    <div class="price-unit">/DAY</div>
  </div>

  <div class="fleet-gallery">
    <div class="fleet-photo suv-gray" role="img" aria-label="Gray SUV on the lot"></div>
    <div class="fleet-photo sedan-blue" role="img" aria-label="Blue sedan on the lot"></div>
    <div class="fleet-photo sedan-red" role="img" aria-label="Red sedan by the office"></div>
    <div class="fleet-photo suv-silver" role="img" aria-label="Silver SUV on the lot"></div>
  </div>

  <div class="offer">
    <h2 class="offer-title">WE CAN OFFER:</h2>
    <ul class="offer-list">
      <li>compact cars</li>
      <li>mid-size sedans</li>
      <li>full size sedans</li>
      <li>SUV</li>
    </ul>
  </div>

  <svg class="ribbons" viewBox="0 0 774 120" aria-hidden="true">
    <g transform="rotate(-3.6 387 60)">
      <rect x="-20" y="48" width="820" height="36" fill="#2fad4e"/>
      <text class="ribbon-text" x="-30" y="73">CAR RENTAL · CAR RENTAL · CAR RENTAL · CAR RENTAL · CAR RENTAL · CAR RENTAL ·</text>
    </g>
    <g transform="rotate(3 387 60)">
      <rect x="-20" y="40" width="820" height="38" fill="#0d4fa8"/>
      <text class="ribbon-text" x="-40" y="66">RENTAL · CAR RENTAL · CAR RENTAL · CAR RENTAL · CAR RENTAL · CAR RENTAL ·</text>
    </g>
  </svg>

  <div class="contact">
    <div class="contact-phone">
      <svg width="26" height="28" viewBox="0 0 24 24"><path d="M6.6 10.8a15.1 15.1 0 0 0 6.6 6.6l2.2-2.2a1 1 0 0 1 1-.25 11.4 11.4 0 0 0 3.6.57 1 1 0 0 1 1 1V20a1 1 0 0 1-1 1A17 17 0 0 1 3 4a1 1 0 0 1 1-1h3.5a1 1 0 0 1 1 1c0 1.25.2 2.45.57 3.57a1 1 0 0 1-.25 1z" fill="#ffffff" stroke="#0d4fa8" stroke-width="1.2"/></svg>
      256-555-0147
    </div>
    <div class="contact-address">
      <svg width="20" height="28" viewBox="0 0 20 28"><path d="M10 1a8.5 8.5 0 0 0-8.5 8.5C1.5 16 10 26 10 26s8.5-10 8.5-16.5A8.5 8.5 0 0 0 10 1z" fill="#ffffff" stroke="#0d4fa8" stroke-width="2"/><circle cx="10" cy="9.5" r="3.2" fill="#0d4fa8"/></svg>
      <p>875 Lakeside Parkway<br>Huntsville, AL 35801</p>
    </div>
  </div>
</div>
</body>
</html>
```